Premium sneaker cleaning kit Packaging Design

We are a sneaker cleaning service and solution provider that is based in New York. We are in need of an elegant and trendy looking packaging design for our premium sneaker cleaning kit. You are to remove all of the graphics from the sample box packaging but keeping all measurements the same; (please note the front of the box has a film of plastic and is see- through) then add in your creativity and graphic with all of our requirements. Our target customers are sneaker-heads everywhere. Good luck.

Target Market(s)

Sneaker-heads in the USA

Industry/Entity Type

Beauty

Font styles to use
Sans Serif

Colors

Designer to choose colors to be used in the design.

Requirements
Must have
• All of the language provided in the word document.
• The name of the product is TOVANE B PREMIUM SNEAKER CLEANING KIT
Nice to have
• Unique simple graphics to go with the use instructions.
Should not have
• Do not need to show the cleaning solution or the brush because the front plastic film is see-through.

```html
<!DOCTYPE html>
<html lang="en">
<head>
<meta charset="utf-8">
<title>TOVANE B Premium Sneaker Cleaning Kit – Box Layout</title>
<link href="https://fonts.googleapis.com/css2?family=Montserrat:wght@400;600;800;900&display=swap" rel="stylesheet">
<style>
  :root {
    --ink: #111111;
    --paper: #ffffff;
    --stage: #e6e6e6;
    --grey: #8a8a8a;
    --soft: #d9d9d9;
  }
  * { margin: 0; padding: 0; box-sizing: border-box; }
  html, body { width: 835px; height: 1200px; overflow: hidden; }
  body {
    background: var(--stage);
    font-family: "Montserrat", Arial, sans-serif;
    color: var(--ink);
    position: relative;
  }
  .dieline { position: absolute; left: 20px; top: 380px; width: 795px; height: 440px; }

  .panel { position: absolute; top: 20px; height: 340px; }
  .panel--front { left: 0; width: 380px; background: var(--paper); }
  .panel--back { left: 380px; width: 320px; background: var(--ink); color: var(--paper); }
  .panel--side { left: 700px; width: 95px; background: var(--ink); color: var(--paper); border-left: 1px solid #333; }
  .flap--top { position: absolute; left: 420px; top: 0; width: 240px; height: 20px; background: var(--paper); border-radius: 6px 6px 0 0; }
  .flap--bottom { position: absolute; left: 0; top: 360px; width: 380px; height: 70px; background: var(--ink);
    clip-path: polygon(0 0, 100% 0, 92% 100%, 8% 100%); }
  .flap--bottom-side { position: absolute; left: 700px; top: 360px; width: 95px; height: 40px; background: var(--ink);
    clip-path: polygon(0 0, 100% 0, 85% 100%, 15% 100%); }

  .brand { display: flex; align-items: center; gap: 6px; font-weight: 900; letter-spacing: 1px; }
  .brand__mark { width: 10px; height: 10px; background: currentColor; }
  .tagline { font-size: 6px; letter-spacing: 2px; color: var(--grey); margin-top: 2px; }

  .front__header { position: absolute; left: 22px; top: 20px; }
  .front__header .brand { font-size: 26px; }
  .product-title { font-weight: 900; font-size: 17px; line-height: 1.05; margin-top: 10px; width: 200px; }
  .revives { margin-top: 8px; font-size: 8px; width: 200px; line-height: 1.35; }
  .revives strong { display: block; font-weight: 900; font-size: 9px; }

  .window { position: absolute; left: 22px; top: 160px; width: 200px; height: 90px; border: 1.5px solid var(--ink); background: var(--paper); }
  .sneaker-art { position: absolute; left: 22px; top: 262px; width: 210px; height: 70px; background: var(--ink); border-radius: 4px 40px 4px 4px; }
  .laces-art { position: absolute; left: 300px; top: 16px; width: 62px; height: 310px; background: linear-gradient(180deg, #2a2a2a, #000); }

  .back__header { margin: 16px 16px 0; background: var(--paper); color: var(--ink); border-radius: 6px; padding: 12px 14px; }
  .back__header .brand { font-size: 20px; }
  .back__header .product-title { font-size: 13px; width: auto; margin-top: 6px; }
  .back__header .revives { width: auto; font-size: 7px; margin-top: 5px; }

  .instructions__title { text-align: center; font-weight: 800; font-size: 10px; letter-spacing: 1.5px; margin: 12px 0 8px; }
  .steps { display: grid; grid-template-columns: repeat(3, 1fr); gap: 8px 8px; padding: 0 16px; }
  .step { text-align: center; }
  .step__art { height: 30px; background: #3a3a3a; border-radius: 3px; }
  .step__text { font-size: 5.5px; line-height: 1.3; margin-top: 3px; }
  .warning { position: absolute; left: 16px; right: 16px; bottom: 12px; background: var(--paper); color: var(--ink);
    font-weight: 800; font-size: 8px; text-align: center; padding: 5px 0; letter-spacing: .5px; }

  .side__text { padding: 14px 8px; font-size: 5.5px; line-height: 1.45; }
  .side__text h3 { font-size: 6.5px; font-weight: 800; margin: 6px 0 2px; }
  .side__text .brand { font-size: 8px; margin-top: 10px; }
  .side__text .brand__mark { width: 6px; height: 6px; }
</style>
</head>
<body>
  <main class="dieline">
    <div class="flap--top"></div>

    <section class="panel panel--front">
      <header class="front__header">
        <div class="brand"><span class="brand__mark"></span>TOVANE B</div>
        <p class="tagline">RESTORE. REFRESH. REVIVE.</p>
        <h1 class="product-title">PREMIUM SNEAKER CLEANING KIT</h1>
        <p class="revives"><strong>REVIVES</strong>Nubuck, Suede, Canvas, Nylon, Leather, Mesh, Fabric, Fleece and many more</p>
      </header>
      <div class="window" aria-hidden="true"></div>
      <div class="sneaker-art" role="img" aria-label="Black sneaker illustration"></div>
      <div class="laces-art" role="img" aria-label="Crossed shoelace pattern"></div>
    </section>

    <section class="panel panel--back">
      <div class="back__header">
        <div class="brand"><span class="brand__mark"></span>TOVANE B</div>
        <h2 class="product-title">PREMIUM SNEAKER CLEANING KIT</h2>
        <p class="revives"><strong>REVIVES</strong>Nubuck, Suede, Canvas, Nylon, Leather, Mesh, Fabric, Fleece and many more</p>
      </div>
      <h2 class="instructions__title">CLEANING INSTRUCTIONS</h2>
      <div class="steps">
        <div class="step"><div class="step__art" role="img" aria-label="Removing laces"></div><p class="step__text">Remove laces and brush off dirt</p></div>
        <div class="step"><div class="step__art" role="img" aria-label="Dipping brush in solution"></div><p class="step__text">Dip brush in solution and water</p></div>
        <div class="step"><div class="step__art" role="img" aria-label="Scrubbing sneaker upper"></div><p class="step__text">Scrub upper in small circles</p></div>
        <div class="step"><div class="step__art" role="img" aria-label="Cleaning the sole"></div><p class="step__text">Clean midsole and outsole well</p></div>
        <div class="step"><div class="step__art" role="img" aria-label="Wiping with towel"></div><p class="step__text">Wipe away foam with towel</p></div>
        <div class="step"><div class="step__art" role="img" aria-label="Sneakers drying"></div><p class="step__text">Let sneakers air dry fully</p></div>
      </div>
      <p class="warning">KEEP OUT OF THE REACH OF CHILDREN</p>
    </section>

    <section class="panel panel--side">
      <div class="side__text">
        <h3>INGREDIENTS</h3>
        <p>Water, coconut surfactant, glycerin, natural fragrance</p>
        <h3>DIRECTIONS</h3>
        <p>Shake well before every use</p>
        <div class="brand"><span class="brand__mark"></span>TOVANE B</div>
        <p>Brooklyn, NY 11201</p>
        <p>Made in USA</p>
      </div>
    </section>

    <div class="flap--bottom"></div>
    <div class="flap--bottom-side"></div>
  </main>
</body>
</html>
```